Improving the design of the attached webpage jpg image

Make the page professional, but keep it simple. All elements on the page can be changed to anything you like EXCEPT the blue bar at the top of the page.

The two images are the same page.

The content on the page must all be there. Do not add new content.

The design needs to feel like a professional score report.
Updates

Need extra days to review

Industry/Entity Type

Education

Number of Pages Required

1 page

Colors

Designer to choose colors to be used in the design.

Requirements
Must have
• The blue bar color and the bars themselves at the top and bottom of the page. All the content on the page.

```html
<!DOCTYPE html>
<html lang="en">
<head>
<meta charset="utf-8">
<title>ScoreWise GAT Score Report</title>
<link href="https://fonts.googleapis.com/css2?family=Figtree:wght@400;500;600;700&family=Lexend:wght@500;600&display=swap" rel="stylesheet">
<style>
:root{
  --brand:#3d7589;
  --brand-dark:#234e60;
  --brand-soft:#e3eff3;
  --page:#f4f8fa;
  --card:#ffffff;
  --line:#e2e9ed;
  --track:#d6e3e8;
  --text:#14232b;
  --muted:#5f6f77;
  --faint:#94a3aa;
  --area-light:#b7cdd5;
  --area-dark:#6f98a8;
}
*{box-sizing:border-box;margin:0;padding:0}
html,body{width:933px;height:1200px;overflow:hidden}
body{background:var(--page);font-family:"Figtree",sans-serif;color:var(--text);position:relative}
.top-bar{position:absolute;left:0;top:0;width:933px;height:58px;background:var(--brand)}
.bottom-bar{position:absolute;left:0;top:1175px;width:933px;height:25px;background:var(--brand)}

.report-title{position:absolute;left:53px;top:78px;font-family:"Lexend",sans-serif;font-weight:600;font-size:22px;color:var(--brand-dark);letter-spacing:-.3px}

.progress{position:absolute;left:53px;top:118px;width:827px;height:34px}
.progress-track{position:absolute;left:0;right:0;top:24px;height:6px;background:var(--track);border-radius:3px}
.progress-fill{position:absolute;left:0;width:640px;top:24px;height:6px;background:var(--brand);border-radius:3px}
.progress-dot{position:absolute;left:632px;top:19px;width:16px;height:16px;border-radius:50%;background:var(--card);border:4px solid var(--brand)}
.progress-label{position:absolute;left:622px;top:0;width:36px;height:16px;line-height:16px;text-align:center;border-radius:8px;background:var(--brand);color:#fff;font-size:10px;font-weight:700}

.test-meta{position:absolute;left:53px;top:166px;font-size:13px;font-weight:600;display:flex;align-items:center;gap:8px;color:var(--text)}
.test-desc{position:absolute;left:53px;top:190px;width:827px;font-size:12px;line-height:20px;color:var(--muted)}

.tabs{position:absolute;left:53px;top:248px;display:flex;gap:4px;padding:4px;background:var(--card);border:1px solid var(--line);border-radius:9px}
.tab{height:30px;padding:0 16px;display:flex;align-items:center;border-radius:6px;font-size:12px;font-weight:600;color:var(--brand)}
.tab.active{background:var(--brand);color:#fff}

.card{position:absolute;left:53px;width:827px;background:var(--card);border:1px solid var(--line);border-radius:12px;box-shadow:0 2px 8px rgba(35,78,96,.07);overflow:hidden}
.card-head{height:44px;display:flex;align-items:center;gap:10px;padding:0 22px;border-bottom:1px solid var(--line);font-weight:700;font-size:14px;color:var(--brand-dark)}
.card-head::before{content:"";width:4px;height:16px;border-radius:2px;background:var(--brand)}

.perf-card{top:312px;height:322px}
.perf-table{width:100%;border-collapse:collapse;table-layout:fixed}
.perf-table th{height:36px;background:var(--page);color:var(--muted);font-weight:600;font-size:11px;letter-spacing:.6px;text-transform:uppercase;text-align:left;padding:0 22px;border-bottom:1px solid var(--line)}
.perf-table th.center,.perf-table td.center{text-align:center}
.perf-table td{height:60px;font-size:13.5px;font-weight:500;padding:0 22px;border-bottom:1px solid var(--line)}
.perf-table tbody tr:last-child td{border-bottom:none}
.perf-table tbody tr:first-child td{font-weight:700}
.perf-table td.scale-cell{padding:0}
.pill{display:inline-block;min-width:52px;height:24px;line-height:24px;padding:0 10px;border-radius:12px;background:var(--brand-soft);color:var(--brand-dark);font-size:12.5px;font-weight:700}
.scale{display:block;width:377px;height:60px}

.dist-card{top:652px;height:480px}
.dist-stats{position:absolute;left:22px;top:60px;display:flex;gap:12px}
.stat{width:190px;height:56px;padding:9px 14px;border-radius:8px;background:var(--page);border:1px solid var(--line);display:flex;flex-direction:column;justify-content:center;gap:2px}
.stat-label{font-size:11px;font-weight:600;color:var(--muted);letter-spacing:.3px}
.stat-value{font-size:20px;font-weight:700;color:var(--brand-dark);line-height:1}
.dist-chart{position:absolute;left:0;top:132px;width:827px;height:340px}
</style>
</head>
<body>
<div class="top-bar"></div>

<h1 class="report-title">ScoreWise GAT Score Report</h1>

<div class="progress">
  <div class="progress-track"></div>
  <div class="progress-fill"></div>
  <div class="progress-dot"></div>
  <span class="progress-label">275</span>
</div>

<p class="test-meta">
  <svg width="13" height="13" viewBox="0 0 12 12" aria-hidden="true"><rect x="0.5" y="1.5" width="11" height="10" rx="1" fill="none" stroke="#3d7589"/><rect x="0.5" y="1.5" width="11" height="2.5" fill="#3d7589"/><rect x="2.5" y="0" width="1.5" height="3" fill="#3d7589"/><rect x="8" y="0" width="1.5" height="3" fill="#3d7589"/></svg>
  September 4, 2024, Simulation Test 2, 275/805
</p>

<p class="test-desc">This is text describing the test details. This is text describing the test details. This is text describing the test details. This is text describing the test details. This is text describing the test details.</p>

<nav class="tabs">
  <span class="tab active">Overall Performance</span>
  <span class="tab">Quantitative Reasoning</span>
  <span class="tab">Verbal Reasoning</span>
  <span class="tab">Data Insights</span>
</nav>

<section class="card perf-card">
  <div class="card-head">Section Performance</div>
  <table class="perf-table">
    <colgroup><col style="width:260px"><col style="width:190px"><col></colgroup>
    <thead><tr><th>Section</th><th class="center">Your Percentile</th><th>Your Score</th></tr></thead>
    <tbody>
      <tr><td>Overall Performance</td><td class="center"><span class="pill">1 th</span></td><td class="scale-cell">
        <svg class="scale" viewBox="0 0 377 60" font-family="Figtree,sans-serif"><line x1="30" y1="32" x2="330" y2="32" stroke="var(--track)" stroke-width="4" stroke-linecap="round"/><line x1="30" y1="32" x2="65" y2="32" stroke="var(--brand)" stroke-width="4" stroke-linecap="round"/><line x1="200" y1="27" x2="200" y2="37" stroke="var(--faint)" stroke-width="1"/><circle cx="65" cy="32" r="6" fill="var(--brand)" stroke="#fff" stroke-width="2"/><text x="65" y="19" font-size="10" font-weight="700" fill="var(--text)" text-anchor="middle">275</text><text x="30" y="50" font-size="9" fill="var(--faint)" text-anchor="middle">205</text><text x="200" y="50" font-size="9" fill="var(--faint)" text-anchor="middle">546</text><text x="348" y="35" font-size="9" fill="var(--faint)" text-anchor="middle">805</text></svg>
      </td></tr>
      <tr><td>Quantitative Reasoning</td><td class="center"><span class="pill">2 nd</span></td><td class="scale-cell">
        <svg class="scale" viewBox="0 0 377 60" font-family="Figtree,sans-serif"><line x1="30" y1="32" x2="330" y2="32" stroke="var(--track)" stroke-width="4" stroke-linecap="round"/><line x1="30" y1="32" x2="60" y2="32" stroke="var(--brand)" stroke-width="4" stroke-linecap="round"/><line x1="210" y1="27" x2="210" y2="37" stroke="var(--faint)" stroke-width="1"/><circle cx="60" cy="32" r="6" fill="var(--brand)" stroke="#fff" stroke-width="2"/><text x="60" y="19" font-size="10" font-weight="700" fill="var(--text)" text-anchor="middle">63</text><text x="30" y="50" font-size="9" fill="var(--faint)" text-anchor="middle">60</text><text x="210" y="50" font-size="9" fill="var(--faint)" text-anchor="middle">78</text><text x="348" y="35" font-size="9" fill="var(--faint)" text-anchor="middle">90</text></svg>
      </td></tr>
      <tr><td>Verbal Reasoning</td><td class="center"><span class="pill">1 th</span></td><td class="scale-cell">
        <svg class="scale" viewBox="0 0 377 60" font-family="Figtree,sans-serif"><line x1="30" y1="32" x2="330" y2="32" stroke="var(--track)" stroke-width="4" stroke-linecap="round"/><line x1="30" y1="32" x2="80" y2="32" stroke="var(--brand)" stroke-width="4" stroke-linecap="round"/><line x1="210" y1="27" x2="210" y2="37" stroke="var(--faint)" stroke-width="1"/><circle cx="80" cy="32" r="6" fill="var(--brand)" stroke="#fff" stroke-width="2"/><text x="80" y="19" font-size="10" font-weight="700" fill="var(--text)" text-anchor="middle">65</text><text x="30" y="50" font-size="9" fill="var(--faint)" text-anchor="middle">60</text><text x="210" y="50" font-size="9" fill="var(--faint)" text-anchor="middle">78</text><text x="348" y="35" font-size="9" fill="var(--faint)" text-anchor="middle">90</text></svg>
      </td></tr>
      <tr><td>Data Insights</td><td class="center"><span class="pill">5 th</span></td><td class="scale-cell">
        <svg class="scale" viewBox="0 0 377 60" font-family="Figtree,sans-serif"><line x1="30" y1="32" x2="330" y2="32" stroke="var(--track)" stroke-width="4" stroke-linecap="round"/><line x1="30" y1="32" x2="60" y2="32" stroke="var(--brand)" stroke-width="4" stroke-linecap="round"/><line x1="210" y1="27" x2="210" y2="37" stroke="var(--faint)" stroke-width="1"/><circle cx="60" cy="32" r="6" fill="var(--brand)" stroke="#fff" stroke-width="2"/><text x="60" y="19" font-size="10" font-weight="700" fill="var(--text)" text-anchor="middle">63</text><text x="30" y="50" font-size="9" fill="var(--faint)" text-anchor="middle">60</text><text x="210" y="50" font-size="9" fill="var(--faint)" text-anchor="middle">78</text><text x="348" y="35" font-size="9" fill="var(--faint)" text-anchor="middle">90</text></svg>
      </td></tr>
    </tbody>
  </table>
</section>

<section class="card dist-card">
  <div class="card-head">Score Distribution</div>
  <div class="dist-stats">
    <div class="stat"><span class="stat-label">Your Score:</span><span class="stat-value">275</span></div>
    <div class="stat"><span class="stat-label">Your Percentile:</span><span class="stat-value">1 th</span></div>
  </div>
  <svg class="dist-chart" viewBox="0 0 827 340" font-family="Figtree,sans-serif">
    <g stroke="var(--line)" stroke-width="1">
      <line x1="70" y1="20" x2="800" y2="20"/><line x1="70" y1="66.6" x2="800" y2="66.6"/><line x1="70" y1="113.3" x2="800" y2="113.3"/><line x1="70" y1="160.8" x2="800" y2="160.8"/><line x1="70" y1="206.6" x2="800" y2="206.6"/><line x1="70" y1="253.2" x2="800" y2="253.2"/>
    </g>
    <g font-size="11" fill="var(--muted)" text-anchor="end">
      <text x="58" y="24">275</text><text x="58" y="70.6">150</text><text x="58" y="117.3">100</text><text x="58" y="164.8">50</text><text x="58" y="210.6">20</text><text x="58" y="257.2">10</text><text x="58" y="304">0</text>
    </g>
    <g transform="translate(-82.6 -1032.4) scale(0.872 0.848)">
      <polygon fill="var(--area-light)" points="175,1331 292,1347 391,1421 502,1374 567,1407 620,1377 643,1332 740,1341 779,1321 861,1366 924,1329 1012,1356 1012,1571 175,1571"/>
      <polygon fill="var(--area-dark)" points="175,1463 295,1478 391,1555 502,1503 567,1539 623,1508 640,1465 740,1474 779,1451 861,1500 924,1461 1012,1488 1012,1571 175,1571"/>
      <polyline fill="none" stroke="var(--brand-dark)" stroke-width="2.5" vector-effect="non-scaling-stroke" stroke-linejoin="round" points="175,1331 292,1347 391,1421 502,1374 567,1407 620,1377 643,1332 740,1341 779,1321 861,1366 924,1329 1012,1356"/>
      <g fill="#fff" stroke="var(--brand-dark)" stroke-width="2" vector-effect="non-scaling-stroke">
        <circle cx="292" cy="1347" r="5.5"/><circle cx="391" cy="1421" r="5.5"/><circle cx="502" cy="1374" r="5.5"/><circle cx="567" cy="1407" r="5.5"/><circle cx="620" cy="1377" r="5.5"/><circle cx="643" cy="1332" r="5.5"/><circle cx="740" cy="1341" r="5.5"/><circle cx="779" cy="1321" r="5.5"/><circle cx="861" cy="1366" r="5.5"/><circle cx="924" cy="1329" r="5.5"/>
      </g>
    </g>
    <line x1="70" y1="300" x2="800" y2="300" stroke="var(--faint)" stroke-width="1"/>
    <g font-size="11" font-weight="600" fill="var(--muted)" text-anchor="middle">
      <text x="104" y="322">January 8,2024</text><text x="262" y="322">March 10,2024</text><text x="420" y="322">July 11,2024</text><text x="589" y="322">Augest 12,2024</text><text x="742" y="322">Sept 10,2024</text>
    </g>
  </svg>
</section>

<div class="bottom-bar"></div>
</body>
</html>
```